International Supplement Company Requires Re-design of Product Label

We are a company that manufactures and sells Nutritional Supplements. We have a wide range of products suitable for all different health needs; sports, wellbeing, weight-loss, ailments. The label needs to be suitable for all varieties of product.
We are looking to update our current supplement bottle labels to make our products appear more attractive and eye catching. We find our current label boring and it doesn’t stand out well when mixed with other competitor products on sites such as Pelmora and Gadlux.
We use flat postal pack bottles which are postal friendly and fit through a letterbox. Our product bottles contain a front and a back label. The bottles can be seen on our website – www.torvanta.co.uk. It is the label on the front of our bottle which we require re-designing. The back contains all of the ingredients, directions, expiry, company info etc and is therefore font only and can be easily designed and laid out by us.
We have two sizes of labels – the first is 66mm by 86mm in size and the second is 86mm by 150mm. The design has to be transferrable from one size to the other.
We are looking for a design that is eye catching, memorable and which reflects quality and trust. We would like a clean, straight look with good strong colours. Our products are sold in shops and over the internet. The label design therefore needs to make our product stand out whether on a shop shelf, on a website or on a flyer.
Most of our products are unisex and not therefore targeted at any particular gender. We do however find that our range of sports supplements is purchased more predominantly by males and could therefore stand a slight variation in colour perhaps to make it a little more masculine.
We would like the range of sports supplements to stand out from the other products and would therefore ask that a slight variation be considered for this. We have considered using a darker colours and/or background on the sports range.
The product titles can vary immensely and have a different amount of characters and numbers in each. Some have very short titles (such as ‘Zinc’) whilst others have longer titles (such as ‘Glucosamine 500mg, Chondroitin 100mg & MSM 100mg’). This is something that needs to be considered when designing the area for the title.
The label needs to contain the following information: Product Title; Product Strength (ie mg); GMP logo; Company Logo; Quantity. Please note that some products, when containing more than one ingredient, have the strength written in their title and not listed separately. Please have a look at the different listings on our website to obtain an understanding of this – www.torvanta.co.uk.
We have also considered the use of an image on some of our bottle labels, to depict the main ingredient contained within the product. Not all of the products lend themselves to using an image but some do. Please have a look at some of our competitor labels and see how they use images within their design – www.brimwello.co.uk www.quendrax.co.uk . Products such as Vitamin B Complex and Glucosamine would not lend themselves to having an image but products such as African Mango and Garlic would. We would be happy to source and apply our own images if you choose to produce a design which leaves a space for the image. We believe that the use of an image can sometimes help the product stand out from competitors and can make it more easily identifiable to some customers.
We require the logo to be produced and provided to us in a High Resolution PSD file with editable Layers
Industry/Entity Type
It Company
Logo Text
Torvanta Health & Fitness

```html
<!DOCTYPE html>
<html lang="en">
<head>
<meta charset="utf-8">
<title>Torvanta Health and Fitness – Supplement Labels</title>
<link rel="stylesheet" href="https://fonts.googleapis.com/css2?family=Montserrat:wght@800;900&family=Nunito:wght@700&family=Open+Sans:ital,wght@0,400;0,600;0,700;1,400;1,700;1,800&display=swap">
<style>
  :root {
    --page-bg: #f4f4f4;
    --brand-grey: #8c8c8c;
    --logo-dark: #3c3c3c;
    --mango-green: #1f9e45;
    --mango-top: #fdf7c0;
    --mango-mid: #fbd44a;
    --mango-orange: #f0922b;
    --mango-red: #d73a1f;
    --mango-rim: #f3cf2c;
    --sport-top: #ffffff;
    --sport-tint: #e3eef8;
    --sport-blue: #2a72bb;
    --sport-navy: #0e3f7f;
    --title-blue: #13438c;
    --tick-yellow: #f7d21e;
    --white: #ffffff;
    --badge-red: #c9251f;
  }
  * { box-sizing: border-box; margin: 0; padding: 0; }
  html, body { width: 1200px; height: 1072px; overflow: hidden; }
  body {
    background: radial-gradient(ellipse at 50% 45%, #ffffff 0%, var(--page-bg) 70%);
    font-family: "Open Sans", sans-serif;
    position: relative;
  }
  .label {
    position: absolute;
    top: 254px;
    width: 344px;
    height: 454px;
    border-radius: 10px;
    overflow: hidden;
    box-shadow: 0 6px 18px rgba(0,0,0,0.12);
  }
  .label--mango { left: 154px; border: 3px solid var(--mango-rim); }
  .label--sport { left: 694px; }
  .label__bg { position: absolute; inset: 0; width: 100%; height: 100%; }
  .label__brand {
    position: absolute; top: 22px; left: 0; right: 0;
    display: flex; flex-direction: column; align-items: center;
  }
  .label__brand-row { display: flex; align-items: center; gap: 6px; }
  .label__brand-dot { width: 15px; height: 15px; border-radius: 50%; background: var(--logo-dark); }
  .label__brand-name {
    font-family: "Nunito", sans-serif; font-weight: 700; font-size: 22px;
    color: var(--logo-dark); line-height: 1;
  }
  .label__brand-tag {
    font-size: 8px; font-style: italic; color: var(--logo-dark);
    margin-left: 52px; margin-top: 1px;
  }
  .mango-title {
    position: absolute; top: 64px; left: 0; right: 0; text-align: center;
    font-family: "Montserrat", sans-serif; font-weight: 900;
    color: var(--mango-green); font-size: 42px; line-height: 44px; letter-spacing: 0.5px;
  }
  .mango-image {
    position: absolute; left: 36px; top: 160px; width: 266px; height: 180px;
    border-radius: 50% 45% 40% 40%;
    background: radial-gradient(ellipse at 50% 45%, #f7b431 0%, #f2952a 45%, rgba(225,90,40,0.55) 75%, rgba(240,150,40,0) 100%);
  }
  .sport-title {
    position: absolute; top: 96px; left: 0; right: 0; text-align: center;
    font-weight: 800; font-style: italic; font-size: 30px; color: var(--title-blue);
    letter-spacing: -0.3px;
  }
  .sport-sub {
    position: absolute; top: 136px; left: 0; right: 0; text-align: center;
    font-size: 19px; color: #333;
  }
  .molecule-image {
    position: absolute; left: 92px; top: 160px; width: 176px; height: 150px;
    border-radius: 50%;
    background: radial-gradient(circle at 50% 50%, #cfe6e8 0%, #a9d3d6 40%, rgba(190,225,230,0) 75%);
  }
  .benefits {
    position: absolute; left: 8px; top: 322px; width: 150px; list-style: none;
    font-size: 7.2px; line-height: 8.4px; color: var(--white); font-weight: 600;
  }
  .benefits li { position: relative; padding-left: 11px; }
  .benefits svg { position: absolute; left: 0; top: 1px; }
  .supplement-info {
    position: absolute; left: 208px; top: 350px; width: 122px;
    color: var(--white); font-style: italic; font-size: 14px; line-height: 17px;
  }
  .storage-note {
    position: absolute; right: 8px; top: 402px; width: 140px;
    color: var(--white); font-style: italic; font-size: 7.4px; line-height: 9px; text-align: right;
  }
  .cert-badge {
    position: absolute; left: 14px; top: 392px; width: 32px; height: 32px; border-radius: 50%;
    background: var(--badge-red); border: 3px solid var(--white);
  }
  .company-mark {
    position: absolute; left: 0; right: 0; top: 812px;
    display: flex; flex-direction: column; align-items: center;
  }
  .company-mark__row { display: flex; align-items: center; gap: 18px; }
  .company-mark__dot { width: 70px; height: 70px; border-radius: 50%; background: var(--brand-grey); }
  .company-mark__name {
    font-family: "Nunito", sans-serif; font-weight: 700; font-size: 118px;
    color: var(--brand-grey); line-height: 1;
  }
  .company-mark__tag {
    font-style: italic; font-size: 36px; color: var(--brand-grey);
    margin-left: 250px; margin-top: -4px;
  }
</style>
</head>
<body>

  <section class="label label--mango">
    <svg class="label__bg" viewBox="0 0 338 448" preserveAspectRatio="none" aria-hidden="true">
      <defs>
        <linearGradient id="mangoTop" x1="0" y1="0" x2="0" y2="1">
          <stop offset="0" stop-color="var(--mango-top)"/>
          <stop offset="0.45" stop-color="var(--mango-mid)"/>
          <stop offset="1" stop-color="var(--mango-orange)"/>
        </linearGradient>
        <linearGradient id="mangoBottom" x1="0" y1="0" x2="0" y2="1">
          <stop offset="0" stop-color="var(--mango-orange)"/>
          <stop offset="1" stop-color="var(--mango-red)"/>
        </linearGradient>
      </defs>
      <rect width="338" height="448" fill="url(#mangoTop)"/>
      <path d="M0 165 L169 332 L338 165 L338 448 L0 448 Z" fill="url(#mangoBottom)"/>
      <path d="M0 165 L169 332 L338 165 M169 332 L169 448" fill="none" stroke="#ffffff" stroke-width="3" stroke-opacity="0.85"/>
    </svg>
    <div class="label__brand">
      <div class="label__brand-row"><span class="label__brand-dot"></span><span class="label__brand-name">Torvanta</span></div>
      <span class="label__brand-tag">Health and Fitness</span>
    </div>
    <h1 class="mango-title">AFRICAN<br>MANGO</h1>
    <div class="mango-image" role="img" aria-label="Photo of whole and sliced ripe mangoes"></div>
    <ul class="benefits">
      <li><svg width="8" height="7" viewBox="0 0 8 7"><path d="M1 3.5 L3 5.5 L7 1" fill="none" stroke="var(--tick-yellow)" stroke-width="1.6"/></svg>Weight loss aid</li>
      <li><svg width="8" height="7" viewBox="0 0 8 7"><path d="M1 3.5 L3 5.5 L7 1" fill="none" stroke="var(--tick-yellow)" stroke-width="1.6"/></svg>Thermogenic properties means it may help to increase body's metabolic rate</li>
      <li><svg width="8" height="7" viewBox="0 0 8 7"><path d="M1 3.5 L3 5.5 L7 1" fill="none" stroke="var(--tick-yellow)" stroke-width="1.6"/></svg>May help suppress appetite and prevent feelings of hunger</li>
      <li><svg width="8" height="7" viewBox="0 0 8 7"><path d="M1 3.5 L3 5.5 L7 1" fill="none" stroke="var(--tick-yellow)" stroke-width="1.6"/></svg>Can help lower cholesterol</li>
      <li><svg width="8" height="7" viewBox="0 0 8 7"><path d="M1 3.5 L3 5.5 L7 1" fill="none" stroke="var(--tick-yellow)" stroke-width="1.6"/></svg>Can help to increase energy levels</li>
    </ul>
    <p class="supplement-info">Food Supplement<br>1500mg</p>
    <span class="cert-badge" aria-hidden="true"></span>
    <p class="storage-note">For best before date and storage information see reverse label</p>
  </section>

  <section class="label label--sport">
    <svg class="label__bg" viewBox="0 0 344 454" preserveAspectRatio="none" aria-hidden="true">
      <defs>
        <linearGradient id="sportTop" x1="0" y1="0" x2="0" y2="1">
          <stop offset="0" stop-color="var(--sport-tint)"/>
          <stop offset="0.5" stop-color="var(--sport-top)"/>
          <stop offset="1" stop-color="var(--sport-tint)"/>
        </linearGradient>
        <linearGradient id="sportBottom" x1="0" y1="0" x2="0" y2="1">
          <stop offset="0" stop-color="var(--sport-blue)"/>
          <stop offset="1" stop-color="var(--sport-navy)"/>
        </linearGradient>
      </defs>
      <rect width="344" height="454" fill="url(#sportTop)"/>
      <path d="M0 168 L172 336 L344 168 L344 454 L0 454 Z" fill="url(#sportBottom)"/>
      <path d="M0 168 L172 336 L344 168 M172 336 L172 454" fill="none" stroke="#ffffff" stroke-width="3" stroke-opacity="0.85"/>
    </svg>
    <div class="label__brand">
      <div class="label__brand-row"><span class="label__brand-dot"></span><span class="label__brand-name">Torvanta</span></div>
      <span class="label__brand-tag">Health and Fitness</span>
    </div>
    <h1 class="sport-title">Acetyl-LCarnitine</h1>
    <p class="sport-sub">Sport &amp; Fitness</p>
    <div class="molecule-image" role="img" aria-label="Illustration of a molecular structure with glossy spheres"></div>
    <ul class="benefits">
      <li><svg width="8" height="7" viewBox="0 0 8 7"><path d="M1 3.5 L3 5.5 L7 1" fill="none" stroke="var(--tick-yellow)" stroke-width="1.6"/></svg>Weight loss aid</li>
      <li><svg width="8" height="7" viewBox="0 0 8 7"><path d="M1 3.5 L3 5.5 L7 1" fill="none" stroke="var(--tick-yellow)" stroke-width="1.6"/></svg>Thermogenic properties means it may help to increase body's metabolic rate</li>
      <li><svg width="8" height="7" viewBox="0 0 8 7"><path d="M1 3.5 L3 5.5 L7 1" fill="none" stroke="var(--tick-yellow)" stroke-width="1.6"/></svg>May help suppress appetite and prevent feelings of hunger</li>
      <li><svg width="8" height="7" viewBox="0 0 8 7"><path d="M1 3.5 L3 5.5 L7 1" fill="none" stroke="var(--tick-yellow)" stroke-width="1.6"/></svg>Can help lower cholesterol</li>
      <li><svg width="8" height="7" viewBox="0 0 8 7"><path d="M1 3.5 L3 5.5 L7 1" fill="none" stroke="var(--tick-yellow)" stroke-width="1.6"/></svg>Can help to increase energy levels</li>
    </ul>
    <p class="supplement-info">Food Supplement<br>500mg</p>
    <span class="cert-badge" aria-hidden="true"></span>
    <p class="storage-note">For best before date and storage information see reverse label</p>
  </section>

  <footer class="company-mark">
    <div class="company-mark__row"><span class="company-mark__dot"></span><span class="company-mark__name">Torvanta</span></div>
    <span class="company-mark__tag">Health and Fitness</span>
  </footer>

</body>
</html>
```